QVLT Meridian LLC Website

Basic website for a start up business in the defense and federal space. If we could have intelligence analysis and technology as a focus that would be great. Looking to use our core colors but a lighter set of web pages would be preferable

Target Market(s)

Defense

Coding

Coded - Design and coding required

Number of Pages Required

3 page

```html
<!DOCTYPE html>
<html lang="en">
<head>
<meta charset="utf-8">
<title>QVLT Meridian LLC — Defense and Federal Space</title>
<link rel="stylesheet" href="https://fonts.googleapis.com/css2?family=Orbitron:wght@500;700;800&family=Poppins:wght@400;500;600;700&display=swap">
<style>
  :root{
    --ink:#1d1a1c;
    --dark:#221e20;
    --red:#c8143c;
    --red-deep:#a90f31;
    --white:#ffffff;
    --grey:#f1f1f1;
    --text:#4a4a4a;
    --muted:#8a8a8a;
  }
  *{margin:0;padding:0;box-sizing:border-box}
  html,body{width:1200px;height:4190px;overflow:hidden;background:var(--white)}
  body{position:relative;font-family:"Poppins",sans-serif;color:var(--ink)}
  .abs{position:absolute}
  .display{font-family:"Orbitron",sans-serif;font-weight:800;letter-spacing:1px;text-transform:uppercase}
  .btn{position:absolute;display:flex;align-items:center;justify-content:center;font-weight:700;font-size:15px;text-transform:uppercase;letter-spacing:.3px}
  .btn-red{background:var(--red);color:var(--white)}
  .btn-outline{border:2px solid var(--red);color:var(--ink);background:var(--white)}
  .body-copy{font-size:14px;line-height:22px;color:var(--text)}

  /* header */
  .brand{position:absolute;left:89px;top:28px;font-family:"Orbitron",sans-serif;font-weight:700;font-size:22px;color:var(--white);letter-spacing:2px;display:flex;align-items:center;gap:10px}
  .brand-dot{width:12px;height:12px;border-radius:50%;background:var(--red)}
  .nav{position:absolute;top:36px;font-size:13px;font-weight:600;color:var(--white);text-transform:uppercase}
  .nav.active{color:var(--red)}
  .nav-contact{position:absolute;left:979px;top:28px;width:132px;height:36px;border:2px solid var(--red);color:var(--white);font-size:13px;font-weight:600;display:flex;align-items:center;justify-content:center}

  .hero-title{left:89px;top:326px;font-size:50px;line-height:51px;color:var(--white)}
  .section-title{width:1200px;text-align:center;font-size:35px;left:0}

  /* products */
  .product{position:absolute;top:1605px;height:346px;width:232px}
  .product-label{position:absolute;left:21px;bottom:24px;width:189px;height:67px;background:var(--white);padding:14px 22px;font-family:"Orbitron",sans-serif;font-weight:500;font-size:16px;line-height:18px;color:var(--ink)}

  /* news */
  .news-small{position:absolute;left:608px;width:507px;height:205px;background:var(--white);box-shadow:0 6px 24px rgba(0,0,0,.08)}
  .news-small .thumb{position:absolute;left:0;top:0;width:252px;height:205px}
  .news-small .copy{position:absolute;left:291px;top:42px;width:200px}
  .news-small h3{font-family:"Orbitron",sans-serif;font-weight:600;font-size:16px;line-height:20px;text-transform:uppercase}
  .news-small p{font-size:12.5px;line-height:18px;color:var(--text);margin-top:8px}
  .news-small a{display:block;margin-top:8px;font-size:13px;font-weight:600;color:var(--red);text-decoration:none}

  /* footer */
  .foot-head{position:absolute;top:3908px;font-family:"Orbitron",sans-serif;font-weight:600;font-size:18px;color:var(--white)}
  .foot-list{position:absolute;top:3940px;list-style:none;font-size:12.5px;line-height:22px;color:var(--white)}
</style>
</head>
<body>

<!-- hero -->
<svg class="abs" style="left:0;top:0" width="1200" height="840" viewBox="0 0 1200 840">
  <path d="M0 0H1200V488C980 620 560 830 240 834C120 836 40 820 0 805Z" fill="var(--dark)"/>
  <path d="M1200 442V488C980 620 560 830 240 834C470 800 880 640 1200 442Z" fill="var(--red)"/>
</svg>
<div class="abs" role="img" aria-label="Wireframe fighter jet flying through a circular ring over a network of connected points" style="left:423px;top:114px;width:777px;height:420px;background:radial-gradient(ellipse at 60% 50%,rgba(200,20,60,.35),rgba(34,30,32,0) 65%)"></div>

<div class="brand"><span>QVLT MERIDIAN</span><span class="brand-dot"></span></div>
<span class="nav active" style="left:641px">Home</span>
<span class="nav" style="left:709px">What we do</span>
<span class="nav" style="left:829px">About</span>
<span class="nav" style="left:904px">News</span>
<span class="nav-contact">CONTACT</span>

<h1 class="abs display hero-title">Defense<br>and federal<br>space</h1>
<span class="btn btn-red" style="left:91px;top:491px;width:179px;height:46px">Explore more</span>

<!-- about -->
<h2 class="abs display" style="left:124px;top:1070px;font-size:36px">About us</h2>
<p class="abs display" style="left:124px;top:1117px;font-size:19px;font-weight:500">Defence &amp; space technologies</p>
<p class="abs body-copy" style="left:122px;top:1155px;width:486px">Lorem Ipsum is simply dummy text of the printing and typesetting industry. Lorem Ipsum has been the industry's standard dummy text ever since the 1500s, when an unknown printer took a galley of type and scrambled it to make a type specimen book.</p>
<span class="btn btn-outline" style="left:122px;top:1258px;width:146px;height:44px">Read more</span>
<div class="abs" style="left:644px;top:1310px;width:120px;height:120px;background:rgba(200,20,60,.12)"></div>
<div class="abs" role="img" aria-label="Radar array tower mounted on a military vehicle on a grassy hill under blue sky" style="left:675px;top:891px;width:403px;height:514px;background:linear-gradient(180deg,#a9cde6 0%,#cfe2ee 55%,#5d6b4a 78%,#7f9a3e 100%);box-shadow:0 20px 40px rgba(0,0,0,.12)"></div>

<!-- products -->
<h2 class="abs display section-title" style="top:1527px">Product &amp; solutions</h2>
<div class="product" style="left:0" role="img" aria-label="Industrial pipework in blue light"><div style="position:absolute;inset:0;background:linear-gradient(160deg,#1c3d6e,#0d1f3d)"></div><div class="product-label">Heavy<br>Engineering</div></div>
<div class="product" style="left:242px" role="img" aria-label="Spacecraft orbiting Earth with the moon behind"><div style="position:absolute;inset:0;background:linear-gradient(180deg,#05070f,#1b2a4a 70%,#3e6592)"></div><div class="product-label">Defence &amp;<br>Space Optics</div></div>
<div class="product" style="left:485px" role="img" aria-label="Gloved hand on an aircraft control panel"><div style="position:absolute;inset:0;background:linear-gradient(180deg,#6b6a55,#3a3b36)"></div><div class="product-label">Defence<br>Electronics</div></div>
<div class="product" style="left:727px" role="img" aria-label="Electricity pylons across an open field"><div style="position:absolute;inset:0;background:linear-gradient(180deg,#e9ecef 0%,#dfe3e6 70%,#b79a5a 100%)"></div><div class="product-label">EMP<br>Solutions</div></div>
<div class="product" style="left:967px;width:233px" role="img" aria-label="Operator with headset at monitoring screens"><div style="position:absolute;inset:0;background:linear-gradient(160deg,#1a2a44,#0b1322)"></div><div class="product-label">Niche<br>Technologies</div></div>

<!-- intelligence -->
<svg class="abs" style="left:0;top:2010px" width="1200" height="780" viewBox="0 0 1200 780">
  <path d="M0 700C0 300 500 40 1200 20V250C1100 600 600 790 200 770C80 765 0 740 0 700Z" fill="var(--grey)"/>
</svg>
<div class="abs" role="img" aria-label="Communications satellite with dish antenna and solar panels" style="left:0;top:2235px;width:585px;height:472px;background:radial-gradient(ellipse at 50% 50%,#c9ccd2 0%,#8fa6d8 40%,rgba(241,241,241,0) 72%)"></div>
<h2 class="abs display" style="left:629px;top:2228px;font-size:36px;line-height:37px">Intelligence<br>analysis and<br>technology</h2>
<p class="abs body-copy" style="left:632px;top:2346px;width:490px">Lorem Ipsum is simply dummy text of the printing and typesetting industry. Lorem Ipsum has been the industry's standard dummy text ever since the 1500s, when an unknown printer took a galley of type and scrambled it to make a type specimen book.</p>
<span class="btn btn-red" style="left:629px;top:2460px;width:145px;height:46px">Read more</span>

<!-- news -->
<h2 class="abs display section-title" style="top:2897px">Latest news</h2>
<div class="abs" role="img" aria-label="Soldier wearing a virtual reality headset" style="left:89px;top:2977px;width:506px;height:426px;background:linear-gradient(180deg,#2b4c7a 0%,#1a2640 60%,#0e1220 100%)"></div>
<h3 class="abs display" style="left:135px;top:3300px;font-size:29px;color:var(--white);font-weight:700">News heading here</h3>
<p class="abs" style="left:135px;top:3337px;font-size:12.5px;color:var(--white)">Lorem Ipsum is simply dummy text of the printing and typesettin.</p>

<div class="news-small" style="top:2977px">
  <div class="thumb" role="img" aria-label="Soldier touching a glowing holographic interface" style="background:linear-gradient(135deg,#1b2b3a,#4a3d28 60%,#d2a25a)"></div>
  <div class="copy"><h3>News<br>heading here</h3><p>Lorem Ipsum is simply dummy text of the printing and typesetting industry.</p><a>READ MORE</a></div>
</div>
<div class="news-small" style="top:3198px">
  <div class="thumb" role="img" aria-label="City skyline at night with network connections" style="background:linear-gradient(180deg,#0a3d8a,#1a6fd0 60%,#08234d)"></div>
  <div class="copy"><h3>News<br>heading here</h3><p>Lorem Ipsum is simply dummy text of the printing and typesetting industry.</p><a>READ MORE</a></div>
</div>

<!-- footer background -->
<svg class="abs" style="left:0;top:3560px" width="1200" height="630" viewBox="0 0 1200 630">
  <path d="M0 380C400 360 900 200 1200 0V630H0Z" fill="var(--ink)"/>
</svg>

<!-- contact band -->
<div class="abs" style="left:88px;top:3566px;width:1022px;height:192px;background:var(--red)"></div>
<h2 class="abs display" style="left:127px;top:3630px;font-size:30px;line-height:38px;color:var(--white);font-weight:700">Have questions?<br>Please contact us</h2>
<span class="btn" style="left:779px;top:3646px;width:260px;height:39px;background:var(--white);color:var(--ink);font-size:13px">Get in touch with us</span>

<!-- footer -->
<div class="abs" style="left:138px;top:3950px;display:flex;align-items:center;gap:10px;font-family:'Orbitron',sans-serif;font-weight:700;font-size:22px;color:var(--white);letter-spacing:2px"><span>QVLT MERIDIAN</span><span class="brand-dot"></span></div>

<h4 class="foot-head" style="left:429px">USEFUL LINKS</h4>
<ul class="foot-list" style="left:431px"><li>Home</li><li>About Us</li><li>Our Process</li><li>Our Team</li><li>Contact Us</li></ul>

<h4 class="foot-head" style="left:642px">NEWSLETTER</h4>
<p class="abs" style="left:642px;top:3940px;font-size:12.5px;color:var(--white)">Subscribe to our newsletter</p>
<div class="abs" style="left:644px;top:3966px;width:168px;height:34px;background:#2c2a2c;border:1px solid #3a3739;font-size:12px;color:var(--muted);padding:8px 12px">Enter your email</div>
<div class="abs" style="left:811px;top:3966px;width:36px;height:34px;background:var(--red);display:flex;align-items:center;justify-content:center">
  <svg width="14" height="14" viewBox="0 0 14 14"><path d="M1 7L13 1L9 13L7 8Z" fill="var(--white)"/></svg>
</div>

<h4 class="foot-head" style="left:907px">CONTACT US</h4>
<svg class="abs" style="left:906px;top:3943px" width="10" height="14" viewBox="0 0 10 14"><path d="M5 0C2.2 0 0 2.2 0 5C0 8.5 5 14 5 14S10 8.5 10 5C10 2.2 7.8 0 5 0ZM5 7A2 2 0 1 1 5 3A2 2 0 0 1 5 7Z" fill="var(--red)"/></svg>
<p class="abs" style="left:927px;top:3940px;font-size:12.5px;line-height:22px;color:var(--white)">Some Address here<br>14 Ridgeline Avenue<br>Example</p>
<svg class="abs" style="left:905px;top:4008px" width="12" height="12" viewBox="0 0 12 12"><path d="M2.5 0.5L4.5 3L3.3 4.5C4 6 6 8 7.5 8.7L9 7.5L11.5 9.5L10 11.5C5 11.5 0.5 7 0.5 2Z" fill="var(--red)"/></svg>
<p class="abs" style="left:927px;top:4004px;font-size:12.5px;color:var(--white)">+1 555 010 2468</p>

<div class="abs" style="left:89px;top:4138px;width:1022px;height:1px;background:#3a3739"></div>
<p class="abs" style="left:0;top:4155px;width:1200px;text-align:center;font-size:13px;color:var(--white)">Copyright © 2022 . All Rights Reserved.</p>
<div class="abs" style="left:1118px;top:4124px;width:38px;height:38px;border-radius:50%;background:var(--red);display:flex;align-items:center;justify-content:center">
  <svg width="10" height="7" viewBox="0 0 10 7"><path d="M1 6L5 2L9 6" stroke="var(--white)" stroke-width="1.6" fill="none"/></svg>
</div>

</body>
</html>
```